K.T.Cash Point Business Card

We need a bi-lingual card (spanish/english). Information should be name, hours, services and address/phone. I am including a flyer as a reference--much of the information is included on it (spanish/english as well). THE COMPANY IS CALLED "K.T. CASH POINT" AND WE THINK THAT "K.T." SHOULD SUFFICE AS A LOGO--BUT WE DON'T HAVE THAT FONT NAILED DOWN. Colors should be Green/Blue scale. Happy colors. It's a check cashing business.

```html
<!DOCTYPE html>
<html lang="en">
<head>
<meta charset="utf-8">
<title>K.T. Cash Point Business Card</title>
<link href="https://fonts.googleapis.com/css2?family=Hind:wght@700&family=Roboto:wght@900&family=Montserrat:wght@500&display=swap" rel="stylesheet">
<style>
  :root {
    --stage: #a9a9a9;
    --navy: #213884;
    --red: #e1190c;
    --yellow: #fff200;
    --white: #ffffff;
    --ink: #1a1a1a;
    --sky: #8dd8f1;
  }
  * { margin: 0; padding: 0; box-sizing: border-box; }
  html, body { width: 1200px; height: 487px; overflow: hidden; background: var(--stage); }
  .canvas { position: relative; width: 1200px; height: 487px; }

  .card { position: absolute; width: 451px; height: 258px; overflow: hidden; }

  .card-front {
    left: 101px; top: 108px;
    background: radial-gradient(ellipse 62% 78% at 50% 45%, var(--white) 0%, #e6f7fc 35%, var(--sky) 100%);
  }
  .front-name {
    position: absolute; left: 0; right: 0; top: 95px;
    text-align: center;
    font-family: "Hind", sans-serif; font-weight: 700;
    font-size: 38px; line-height: 1; letter-spacing: 0.2px;
    color: var(--navy);
  }

  .card-back { left: 653px; top: 111px; background: var(--white); }
  .header-band { position: absolute; left: 0; top: 0; }
  .header-accent { position: absolute; left: 0; top: 22px; width: 3px; height: 25px; background: var(--yellow); }
  .back-name {
    position: absolute; left: 23px; top: 24px;
    font-family: "Hind", sans-serif; font-weight: 700;
    font-size: 26px; line-height: 1; color: var(--white);
  }

  .headline {
    position: absolute; left: 22px; top: 112px;
    font-family: "Roboto", sans-serif; font-weight: 900;
    font-size: 29px; line-height: 1; color: var(--red); letter-spacing: 0.3px;
  }
  .taglines {
    position: absolute; left: 26px; top: 145px;
    font-family: "Roboto", sans-serif; font-weight: 900;
    font-size: 13.5px; line-height: 17px; color: var(--navy);
  }
  .spanish-pill {
    position: absolute; left: 26px; top: 184px; width: 138px; height: 21px;
    border-radius: 11px; background: var(--yellow);
    font-family: "Roboto", sans-serif; font-weight: 900;
    font-size: 10.5px; line-height: 21px; color: var(--red); text-align: center;
  }

  .contact-icon { position: absolute; left: 288px; width: 26px; height: 26px; }
  .icon-pin { top: 108px; }
  .icon-phone { top: 153px; }
  .icon-clock { top: 203px; }
  .contact-text {
    position: absolute; left: 321px;
    font-family: "Montserrat", sans-serif; font-weight: 500;
    font-size: 8px; color: var(--ink); white-space: nowrap;
  }
  .address { top: 109px; line-height: 14px; }
  .phone { top: 162px; }
  .hours { top: 205px; line-height: 11px; }
</style>
</head>
<body>
<div class="canvas">

  <section class="card card-front">
    <div class="front-name">K.T. CASH POINT</div>
  </section>

  <section class="card card-back">
    <svg class="header-band" width="451" height="75" viewBox="0 0 451 75">
      <polygon points="0,0 451,0 451,60 283,60 269,75 0,75" fill="var(--navy)"/>
    </svg>
    <div class="header-accent"></div>
    <div class="back-name">K.T. CASH POINT</div>

    <div class="headline">CHECK CA$HING</div>
    <div class="taglines">ALL CHECKS WELCOME!<br>BEST RATES IN MAPLE VALLEY</div>
    <div class="spanish-pill">¡SE HABLA ESPAÑOL!</div>

    <svg class="contact-icon icon-pin" viewBox="0 0 26 26">
      <circle cx="13" cy="13" r="13" fill="var(--navy)"/>
      <path d="M13 6.5a4 4 0 0 0-4 4c0 3 4 8 4 8s4-5 4-8a4 4 0 0 0-4-4z" fill="var(--white)"/>
      <circle cx="13" cy="10.5" r="1.5" fill="var(--navy)"/>
    </svg>
    <div class="contact-text address">482 BIRCH AVENUE<br>MAPLE RIDGE, NY</div>

    <svg class="contact-icon icon-phone" viewBox="0 0 26 26">
      <circle cx="13" cy="13" r="13" fill="var(--navy)"/>
      <path d="M8.6 7.5l2.3-.6 1.3 3-1.4 1.1a8 8 0 0 0 3.9 3.9l1.1-1.4 3 1.3-.6 2.3c-.2.7-.9 1.1-1.6 1-5-.7-8.8-4.5-9.5-9.5-.1-.6.3-1.3 1-1.6z" fill="var(--white)"/>
    </svg>
    <div class="contact-text phone">(555) 014 - 2390</div>

    <svg class="contact-icon icon-clock" viewBox="0 0 26 26">
      <circle cx="13" cy="13" r="13" fill="var(--navy)"/>
      <circle cx="13" cy="13" r="6" fill="none" stroke="var(--white)" stroke-width="1.8"/>
      <path d="M13 9.8V13h-2.4" fill="none" stroke="var(--white)" stroke-width="1.6" stroke-linecap="round"/>
    </svg>
    <div class="contact-text hours">ONDAY-SATURDAY, 9AM-9PM<br>MONDAY-SATURDAY, 9AM-9PM</div>
  </section>

</div>
</body>
</html>
```